Cold Brew coffee needs a label design

Im looking for a label design for my cold brew coffee that has a funky street vibe look and feel about it. I'd like to see some neon colours and black - but am open to other ideas something that will pop. I have 2 flavours so would like to be able to change the flavour and ingredients if you can only produce the one label for when I go to print. My bottles are clear with an aluminium lid.

On the label it needs to have:
- my logo
- the flavour. The flavours are 'black' and 'latte'
- ingredients: signature blend brewed coffee & springwater (for black)
- ingredients: signature blend brewed coffee & full cream milk (for latte)
- 200ml
- @marrowfieldlncoldbrew

The size of the label has to fit to a maximum 60mm wide x 90mm high - Im open to rectangle or circle. Please find attached some pics and files to help with the design.

Requirements
Must have
• A fig tree similar to picture below.
Nice to have
• Would love if the leave could incorporate these colours. Thank you

```html
<!DOCTYPE html>
<html lang="en">
<head>
<meta charset="utf-8">
<title>Marrowfield Ln. Cold Brew – Black label</title>
<link href="https://fonts.googleapis.com/css2?family=Josefin+Sans:wght@700&family=Tinos&display=swap" rel="stylesheet">
<style>
  :root {
    --page: #ffffff;
    --label-black: #141414;
    --wall-dark: #1c1c1c;
    --wall-mid: #2a2a2a;
    --frame-white: #ffffff;
    --bulb-cream: #fde9c4;
    --bulb-orange: #e07a1f;
    --glow: rgba(255, 170, 80, 0.55);
    --pop-pink: #ec1c8c;
    --pop-yellow: #ffe600;
    --pop-cyan: #1fb4e8;
    --pop-red: #e8262a;
    --pop-green: #9ccc3c;
  }
  html, body {
    margin: 0;
    padding: 0;
    width: 1200px;
    height: 1200px;
    overflow: hidden;
    background: var(--page);
  }
  .canvas {
    position: relative;
    width: 1200px;
    height: 1200px;
  }
  .label {
    position: absolute;
    left: 280px;
    top: 120px;
    width: 640px;
    height: 960px;
    border-radius: 28px;
    background: var(--label-black);
    overflow: hidden;
    font-family: "Tinos", "Times New Roman", serif;
    color: var(--frame-white);
  }
  .label__wall {
    position: absolute;
    inset: 0;
    background: radial-gradient(ellipse at 50% 40%, var(--wall-mid) 0%, var(--wall-dark) 60%, var(--label-black) 100%);
  }
  .label__frame {
    position: absolute;
    left: 20px;
    top: 20px;
    right: 20px;
    bottom: 20px;
    border: 3px solid var(--frame-white);
    border-radius: 14px;
  }
  .label__burst {
    position: absolute;
    background: radial-gradient(circle at 30% 30%, var(--pop-yellow) 0%, var(--pop-pink) 35%, var(--pop-cyan) 65%, var(--pop-green) 100%);
  }
  .label__burst--top {
    left: 23px;
    top: 23px;
    width: 164px;
    height: 100px;
    border-radius: 10px 0 100% 0;
  }
  .label__burst--bottom {
    right: 23px;
    bottom: 23px;
    width: 290px;
    height: 180px;
    border-radius: 100% 0 10px 0;
    background: radial-gradient(circle at 75% 80%, var(--pop-yellow) 0%, var(--pop-red) 25%, var(--pop-pink) 45%, var(--pop-cyan) 70%, var(--pop-green) 100%);
  }
  .brand {
    position: absolute;
    left: 0;
    right: 0;
    top: 98px;
    text-align: center;
    font-size: 50px;
    line-height: 1;
    color: var(--frame-white);
  }
  .headline {
    position: absolute;
    left: 0;
    right: 0;
    margin: 0;
    text-align: center;
    font-family: "Josefin Sans", "Arial", sans-serif;
    font-weight: 700;
    line-height: 1;
    color: var(--bulb-cream);
    -webkit-text-stroke: 3px var(--bulb-orange);
    paint-order: stroke fill;
    text-shadow: 0 0 18px var(--glow), 6px 8px 6px rgba(0, 0, 0, 0.7);
  }
  .headline--cold { top: 208px; font-size: 150px; letter-spacing: 8px; }
  .headline--brew { top: 352px; font-size: 150px; letter-spacing: 8px; }
  .headline--coffee { top: 505px; font-size: 110px; letter-spacing: 8px; }
  .flavour {
    position: absolute;
    left: 203px;
    top: 640px;
    width: 235px;
    height: 75px;
    box-sizing: border-box;
    border: 3px solid var(--frame-white);
    display: flex;
    align-items: center;
    justify-content: center;
    font-size: 52px;
    letter-spacing: 1px;
  }
  .ingredients {
    position: absolute;
    left: 42px;
    top: 738px;
    margin: 0;
    font-size: 24px;
    line-height: 1.02;
  }
  .volume {
    position: absolute;
    left: 141px;
    top: 866px;
    font-size: 36px;
    line-height: 1;
  }
</style>
</head>
<body>
<div class="canvas">
  <div class="label">
    <div class="label__wall" role="img" aria-label="Dark painted brick wall texture"></div>
    <div class="label__frame"></div>
    <div class="label__burst label__burst--top" role="img" aria-label="Cluster of bright concentric neon circles"></div>
    <div class="label__burst label__burst--bottom" role="img" aria-label="Cluster of bright concentric neon circles"></div>

    <div class="brand">Marrowfield Ln.</div>

    <h1 class="headline headline--cold">COLD</h1>
    <div class="headline headline--brew">BREW</div>
    <div class="headline headline--coffee">COFFEE</div>

    <div class="flavour">BLACK</div>

    <p class="ingredients">Ingredients:<br>Signature Blend Brewed<br>Coffee &amp; Springwater</p>

    <div class="volume">200ml</div>
  </div>
</div>
</body>
</html>
```